Local Directory Ad

We currently have an advertisement in our local directory (see attached). We would like to make it look more appealing.
Dimensions are 110mm H X 175mm W
We would like to keep the same colours and contact details remain the same.
Most of the content can remain the same, Just remove the line Tax effective remote area salary packaging and add in Self Managed Super Funds.We want to change mortgage broking to Mortgage Broking and Loan Structuring.

We want to change the line Local accountants Local Knowledge Local Experience - to something like local knowledge beyond compare or unsurpassed local knowledge but open to suggestions on this.

there are some good designs posted so far. I particulalry like the ones from marloquip, tovel58, and the last one posted by pruvsomlak and WPH. Keep up the good work guys

```html
<!DOCTYPE html>
<html lang="en">
<head>
<meta charset="utf-8">
<title>Marlowe Accounting &amp; Finance – Directory Ad</title>
<link rel="stylesheet" href="https://fonts.googleapis.com/css2?family=Rubik:wght@300;400;700;800&family=Exo+2:wght@600;700&display=swap">
<style>
  :root {
    --backdrop: #9a9a9a;
    --slate: #3c4a47;
    --red: #cc2229;
    --white: #ffffff;
    --ink: #111111;
    --panel-tint: #f3d4d5;
  }
  * { box-sizing: border-box; margin: 0; padding: 0; }
  html, body { width: 1200px; height: 792px; overflow: hidden; background: var(--backdrop); }
  .ad {
    position: absolute; left: 84px; top: 72px; width: 1032px; height: 648px;
    background: var(--white); overflow: hidden;
  }
  .header-band { position: absolute; left: 0; top: 0; width: 100%; height: 280px; background: var(--slate); }
  .footer-band { position: absolute; left: 0; bottom: 0; width: 100%; height: 18px; background: var(--slate); }
  .business-name {
    position: absolute; top: 72px; width: 100%; text-align: center;
    font-family: "Rubik", sans-serif; font-weight: 700; font-size: 50px;
    color: var(--white); line-height: 1;
  }
  .licence {
    position: absolute; top: 162px; width: 100%; text-align: center;
    font-family: "Rubik", sans-serif; font-weight: 400; font-size: 16px; letter-spacing: 3px; color: var(--white);
  }
  .feature {
    position: absolute; top: 214px; width: 312px; height: 125px;
    background: var(--red); border: 4px solid var(--white); border-radius: 12px;
    display: flex; align-items: center;
  }
  .feature-accountants { left: 37px; }
  .feature-knowledge { left: 360px; }
  .feature-experience { left: 683px; }
  .feature-icon { flex: 0 0 auto; margin-left: 26px; width: 86px; height: 80px; }
  .feature-label {
    margin-left: 18px; font-family: "Rubik", sans-serif; color: var(--white); line-height: 1.05;
  }
  .feature-label span { display: block; font-size: 24px; font-weight: 400; }
  .feature-label strong { display: block; font-size: 29px; font-weight: 700; }
  .services-heading {
    position: absolute; top: 356px; width: 100%; text-align: center;
    font-family: "Rubik", sans-serif; font-weight: 800; font-size: 32px; color: var(--red);
  }
  .services {
    position: absolute; top: 400px; width: 100%; text-align: center;
    font-family: "Rubik", sans-serif; font-weight: 300; font-size: 28px; line-height: 33px; color: var(--ink);
  }
  .contact-col {
    position: absolute; top: 524px; text-align: center; font-style: normal;
    font-family: "Exo 2", sans-serif; font-weight: 700; font-size: 25px; line-height: 30px;
    letter-spacing: 1px; color: var(--ink);
  }
  .address { left: 20px; width: 480px; }
  .reach { left: 520px; width: 480px; }
  .web { color: var(--red); font-size: 28px; letter-spacing: 3px; }
  .divider { position: absolute; left: 508px; top: 532px; width: 6px; height: 98px; background: var(--slate); }
</style>
</head>
<body>
<main class="ad">
  <div class="header-band"></div>
  <h1 class="business-name">Marlowe Accounting &amp; Finance</h1>
  <p class="licence">AUSTRALIAN CREDIT LICENCE 412 608</p>

  <div class="feature feature-accountants">
    <svg class="feature-icon" role="img" aria-label="Illustration of a person reading an open book" viewBox="0 0 86 80"><rect width="86" height="80" rx="8" fill="var(--panel-tint)"/></svg>
    <p class="feature-label"><span>Local</span><strong>Accoutants</strong></p>
  </div>
  <div class="feature feature-knowledge">
    <svg class="feature-icon" role="img" aria-label="Illustration of a stack of books with reading glasses" viewBox="0 0 86 80"><rect width="86" height="80" rx="8" fill="var(--panel-tint)"/></svg>
    <p class="feature-label"><span>Local</span><strong>Knowledge</strong></p>
  </div>
  <div class="feature feature-experience">
    <svg class="feature-icon" role="img" aria-label="Illustration of a certificate with a seal" viewBox="0 0 86 80"><rect width="86" height="80" rx="8" fill="var(--panel-tint)"/></svg>
    <p class="feature-label"><span>Local</span><strong>Experience</strong></p>
  </div>

  <h2 class="services-heading">We are here for you all year round to assist with...</h2>
  <p class="services">
    •Accounting &amp; Taxation •Business Advice •GST and BAS’s<br>
    •Mortgage Broking and Loan Structuring •Bookkeeping<br>
    •Self Managed Super Funds for your employees
  </p>

  <address class="contact-col address">
    Shop 5, Ridge Arcade<br>
    12 Calder St. Port Tavish<br>
    PO Box 418, Port Tavish 6790
  </address>
  <div class="divider"></div>
  <p class="contact-col reach">
    reception@maaf.com.au<br>
    Ph: 9100 2841 Fax: 9100 2842<br>
    <span class="web">www.maaf.com.au</span>
  </p>

  <div class="footer-band"></div>
</main>
</body>
</html>
```